Brantley Yard Services Flyer Design

I need a new flyer design for my business, Brantley Yard Services. I’ll be providing my old flyer and logo as references. The new flyer should feature updated wording, contact information, logos, and photos, but still keep the original “What We Do” section and include the phrase “Don’t See? Just Ask!” somewhere near the services. The flyer needs to look great in black and white for door-to-door handouts but also be eye-catching and professional enough for social media use.

The updated content should include the headline “Transforming Outdoor Spaces with Hard Work & Precision” and highlight three main service areas: Landscaping Services (project-based landscaping to clean, prepare, and transform outdoor spaces with precision), Property Cleanup (quick hauls, debris removal, or full cleanouts—no job too big or small), and Ground Preparation (pad preparation, brush removal, and fire lines—making properties safe, functional, and project-ready).

Please also include a “Why Choose Us?” section that lists: Locally owned since 2022, Reliable & affordable – no corners cut, Professional results you can trust, LICENSED AND Insured, and Quality work / on time / references / flexible / follow-up.

At the bottom, include the contact details: Call or Text Today!
www.brantleyyard.example
| sales@brantleyyard.example
| (555) 014-2793

The overall design should be clean, professional, and easy to read with a layout that clearly shows what we offer. Use visuals that represent outdoor services, landscaping, and property cleanup/prep work. I want something that feels trustworthy, family-friendly, and modern.
Use the same photo of leaf clean up from the original flyer if possible.
Our company colors are also black and white. For the most part.

```html
<!DOCTYPE html>
<html lang="en">
<head>
<meta charset="utf-8">
<title>Brantley Yard Services Flyer</title>
<link href="https://fonts.googleapis.com/css2?family=Syne:wght@400;500;600;700;800&display=swap" rel="stylesheet">
<style>
  :root {
    --ink: #1c1c1c;
    --paper: #ffffff;
    --muted: #a6a6a6;
    --body: #3a3a3a;
    --panel: #333333;
    --rule: #2a2a2a;
    --leaf-a: #6b5a1e;
    --leaf-b: #2f6a6e;
  }
  * { margin: 0; padding: 0; box-sizing: border-box; }
  html, body { width: 924px; height: 1200px; overflow: hidden; background: var(--paper); }
  body { font-family: "Syne", sans-serif; color: var(--ink); }
  .flyer { position: relative; width: 924px; height: 1200px; background: var(--paper); }
  .abs { position: absolute; }

  .brand { left: 110px; top: 150px; width: 350px; display: flex; align-items: center; gap: 14px; }
  .brand-mark { width: 44px; height: 44px; background: var(--ink); flex: none; }
  .brand-name { font-weight: 800; font-size: 30px; line-height: 1.05; color: var(--ink); }

  .header-rule { left: 476px; top: 68px; width: 1.5px; height: 218px; background: var(--rule); }
  .headline { left: 512px; top: 60px; }
  .headline .lead { font-size: 29px; font-weight: 500; line-height: 1; letter-spacing: -0.5px; }
  .headline .big { font-size: 60px; font-weight: 800; font-style: italic; line-height: 1; letter-spacing: -2px; display: block; }
  .headline .big.first { margin-top: 16px; }
  .headline .big.second { margin-left: 44px; margin-top: 0; }
  .headline .tail { font-size: 29px; font-weight: 600; line-height: 1.12; letter-spacing: -1px; margin-top: 14px; }

  .step { top: 320px; width: 240px; }
  .step-num { font-size: 25px; font-weight: 800; color: var(--muted); letter-spacing: -1px; line-height: 1; }
  .step-title { font-size: 21px; font-weight: 600; letter-spacing: -0.6px; margin-top: 10px; white-space: nowrap; }
  .step-text { font-size: 15.5px; line-height: 20px; color: var(--body); margin-top: 10px; letter-spacing: -0.3px; }
  .step-arrow { top: 400px; width: 22px; height: 16px; }

  .services-box { left: 56px; top: 498px; width: 811px; height: 333px; border: 1px solid var(--rule); }
  .services-title { left: 0; width: 811px; top: 28px; text-align: center; font-size: 29px; font-weight: 600; letter-spacing: -1px; }
  .col-head { font-size: 21px; font-weight: 500; letter-spacing: -0.6px; line-height: 1; }
  .col-rule { top: 88px; width: 1px; height: 172px; background: var(--rule); }
  .service-list { list-style: none; }
  .service-list li { display: flex; align-items: flex-start; gap: 9px; font-size: 16px; line-height: 17px; color: var(--body); letter-spacing: -0.3px; margin-bottom: 12px; }
  .service-list svg { width: 14px; height: 14px; flex: none; margin-top: 1px; }
  .ask { left: 0; width: 811px; top: 280px; text-align: center; font-size: 20px; font-weight: 600; letter-spacing: -0.8px; }

  .photo-band { left: 104px; top: 826px; width: 718px; height: 172px; background: var(--panel); }
  .photo { top: 14px; height: 143px; }
  .photo-yard { left: 16px; width: 218px; background: linear-gradient(180deg, #9bb7d2 0%, #6f8a5a 45%, #b79a6d 100%); }
  .photo-haul { left: 250px; width: 220px; background: linear-gradient(180deg, #b89a6a 0%, #7d7a72 50%, #3c4c7a 100%); }
  .photo-leaves { left: 485px; width: 217px; background: linear-gradient(135deg, #3f4a2a 0%, var(--leaf-a) 45%, #c9a22b 65%, var(--leaf-b) 100%); }

  .why { left: 55px; top: 1030px; width: 360px; }
  .why h2 { font-size: 21px; font-weight: 600; letter-spacing: -0.8px; }
  .why p { font-size: 15.5px; line-height: 20px; color: var(--body); margin-top: 10px; letter-spacing: -0.3px; }
  .why strong { color: var(--ink); font-weight: 700; }

  .contact-panel { left: 416px; top: 1020px; width: 449px; height: 135px; background: var(--panel); color: var(--paper); }
  .cta { left: 26px; top: 38px; }
  .cta .small { font-size: 21px; font-weight: 500; letter-spacing: -0.6px; line-height: 1; }
  .cta .large { font-size: 36px; font-weight: 600; letter-spacing: -1.2px; line-height: 1; margin-top: 6px; }
  .contact-list { left: 186px; top: 34px; list-style: none; }
  .contact-list li { display: flex; align-items: center; gap: 8px; font-size: 15px; font-weight: 500; line-height: 1; margin-bottom: 12px; letter-spacing: -0.3px; }
  .contact-list svg { width: 12px; height: 12px; flex: none; fill: var(--paper); }
</style>
</head>
<body>
<main class="flyer">

  <div class="abs brand">
    <span class="brand-mark"></span>
    <span class="brand-name">Brantley Yard Services</span>
  </div>

  <div class="abs header-rule"></div>
  <h1 class="abs headline">
    <span class="lead">Transforming</span>
    <span class="big first">Outdoor</span>
    <span class="big second">Spaces</span>
    <div class="tail">with Hard Work &amp;<br>Precision!</div>
  </h1>

  <section class="abs step" style="left:55px;">
    <div class="step-num">01.</div>
    <h3 class="step-title">Landscaping Services</h3>
    <p class="step-text">Project-based landscaping to clean, prepare, and transform outdoor spaces with precision.</p>
  </section>
  <svg class="abs step-arrow" style="left:358px;" viewBox="0 0 22 16" fill="none" stroke="#1c1c1c" stroke-width="1.8"><path d="M1 8h19M13 1l7 7-7 7"/></svg>
  <section class="abs step" style="left:390px; width:170px;">
    <div class="step-num">02.</div>
    <h3 class="step-title">Property Cleanup</h3>
    <p class="step-text">Quick hauls, debris removal, or full cleanouts no job too big or small.</p>
  </section>
  <svg class="abs step-arrow" style="left:562px;" viewBox="0 0 22 16" fill="none" stroke="#1c1c1c" stroke-width="1.8"><path d="M1 8h19M13 1l7 7-7 7"/></svg>
  <section class="abs step" style="left:592px; width:200px;">
    <div class="step-num">03.</div>
    <h3 class="step-title">Ground Preparation</h3>
    <p class="step-text">Pad preparation, brush removal, and fire lines making properties safe, functional, and project-ready.</p>
  </section>

  <section class="abs services-box">
    <h2 class="abs services-title">What We Do</h2>

    <div class="abs" style="left:34px; top:96px; width:220px;">
      <h3 class="col-head">REMOVE</h3>
      <ul class="service-list" style="margin-top:30px;">
        <li><svg viewBox="0 0 14 14"><rect x="2" y="4" width="10" height="9" fill="#1c1c1c"/><rect x="1" y="2" width="12" height="2" fill="#1c1c1c"/></svg>Junk removal</li>
        <li><svg viewBox="0 0 14 14"><rect x="1" y="4" width="9" height="6" fill="#1c1c1c"/><rect x="10" y="6" width="3" height="4" fill="#1c1c1c"/><circle cx="4" cy="12" r="1.6" fill="#1c1c1c"/><circle cx="11" cy="12" r="1.6" fill="#1c1c1c"/></svg>Trash &amp; waste hauling</li>
        <li><svg viewBox="0 0 14 14"><path d="M3 1v10h9" stroke="#1c1c1c" stroke-width="2" fill="none"/><circle cx="10" cy="6" r="2.5" fill="#1c1c1c"/></svg>Yard and garden<br>cleanup</li>
        <li><svg viewBox="0 0 14 14"><rect x="6" y="3" width="7" height="10" fill="#1c1c1c"/><circle cx="3" cy="3" r="2" fill="#1c1c1c"/><rect x="2" y="6" width="2.5" height="7" fill="#1c1c1c"/></svg>Appliance removal</li>
      </ul>
    </div>
    <div class="abs col-rule" style="left:288px;"></div>

    <div class="abs" style="left:354px; top:96px; width:180px;">
      <h3 class="col-head">INSTALL</h3>
      <ul class="service-list" style="margin-top:30px;">
        <li><svg viewBox="0 0 14 14"><path d="M2 1l6 8" stroke="#1c1c1c" stroke-width="2"/><path d="M4 13h9l-3-5z" fill="#1c1c1c"/></svg>Mulch</li>
        <li><svg viewBox="0 0 14 14"><rect x="1" y="2" width="12" height="10" rx="2" fill="none" stroke="#1c1c1c" stroke-width="1.3"/><rect x="4" y="6" width="6" height="2" fill="#1c1c1c"/></svg>D.G.</li>
        <li><svg viewBox="0 0 14 14"><path d="M7 8V3M7 5c-3-3-5-1-5 0 2 1 4 1 5 0zM7 5c3-3 5-1 5 0-2 1-4 1-5 0z" fill="#1c1c1c" stroke="#1c1c1c"/><path d="M4 9h6l-1 4H5z" fill="#1c1c1c"/></svg>Plants</li>
        <li><svg viewBox="0 0 14 14"><path d="M1 13l5-9 3 4 2-2 3 7z" fill="#1c1c1c"/></svg>Rock</li>
      </ul>
    </div>
    <div class="abs col-rule" style="left:511px;"></div>

    <div class="abs" style="left:552px; top:96px; width:250px;">
      <h3 class="col-head">MAINTENANCE<br>&amp; OTHER</h3>
      <ul class="service-list" style="margin-top:8px;">
        <li><svg viewBox="0 0 14 14"><path d="M2 2l9 9" stroke="#1c1c1c" stroke-width="2"/><path d="M9 9l4 1-1 3-4-1z" fill="#1c1c1c"/></svg>Yard clean up</li>
        <li><svg viewBox="0 0 14 14"><path d="M5 12V5M5 6C2 4 2 2 3 1c2 1 3 3 2 5zM5 7c3-2 5-1 5 0-2 1-4 1-5 0z" fill="#1c1c1c" stroke="#1c1c1c"/><circle cx="11" cy="11" r="2" fill="none" stroke="#1c1c1c" stroke-width="1.3"/></svg>Weed prevention<br>(pre-emergent)</li>
        <li><svg viewBox="0 0 14 14"><path d="M1 5h8v3H1z" fill="#1c1c1c"/><path d="M9 6h3v7" stroke="#1c1c1c" stroke-width="2" fill="none"/></svg>Roof &amp; gutter cleaning</li>
        <li><svg viewBox="0 0 14 14"><path d="M3 1v12M7 1v12M11 1v12M1 5h12M1 10h12" stroke="#1c1c1c" stroke-width="1.4"/></svg>Fence &amp; deck staining</li>
      </ul>
    </div>

    <p class="abs ask">Don’t See? Just Ask!</p>
  </section>

  <div class="abs photo-band">
    <div class="abs photo photo-yard" role="img" aria-label="Finished backyard with gravel patio, retaining wall and wooden fence"></div>
    <div class="abs photo photo-haul" role="img" aria-label="Trailer loaded with hauled junk and old carpet"></div>
    <div class="abs photo photo-leaves" role="img" aria-label="Gloved hand clearing autumn leaves from a roof gutter"></div>
  </div>

  <section class="abs why">
    <h2>Why Choose Us?</h2>
    <p>Locally owned <strong>since 2022, Reliable &amp; affordable</strong> – no corners cut, Professional results you can trust, LICENSED AND Insured, and Quality work / on time / references / flexible / follow-up.</p>
  </section>

  <section class="abs contact-panel">
    <div class="abs cta">
      <div class="small">Call or Text</div>
      <div class="large">Today!</div>
    </div>
    <ul class="abs contact-list">
      <li><svg viewBox="0 0 12 12"><path d="M2 0.5l2.2 0.2 1 2.6-1.4 1.1c.7 1.5 1.9 2.7 3.4 3.4l1.1-1.4 2.6 1 .2 2.2c-.2.9-1 1.4-1.9 1.4C4.6 11 1 7.4.6 2.4.6 1.5 1.1.7 2 .5z"/></svg>(555) 014-2793</li>
      <li><svg viewBox="0 0 12 12"><path d="M0 2h12v1.2L6 7 0 3.2zM0 4.6l6 3.8 6-3.8V10H0z"/></svg>sales@brantleyyard.example</li>
      <li><svg viewBox="0 0 12 12"><path d="M2 0l8 6-3.3.5 2 4-1.4.7-2-4L2 10z"/></svg>www.brantleyyard.example</li>
    </ul>
  </section>

</main>
</body>
</html>
```